OPF - Brochure 52 week Curriculum

Oak Path Fellows, Inc. wants to create a distribution Brochure. In the Bible (Matthew 28:18-20)- JESUS said to "TEACH" others what HE has commanded. we want to "PUT IN PRINT"

these 52 lines summarize HIS teachings
we want to use as our Curriculum teaching men ...

incorporate our statements and two main passages of scripture
(see attach pictures of headquarter lobby) to brand uniformity and consistency... we have summarized into 52 groups, but its NOT required to have numbers...
Purpose = obey GOD
Mission = love others
Vision = Development God fearing men globally.

The designer can have freedom in layout and sizing.
we were thinking bi fold , but again... designer has freedom
Please incorporate our colors (white, black, gray) using color wheel provided and our LOGO with website.

```html
<!DOCTYPE html>
<html lang="en">
<head>
<meta charset="UTF-8">
<title>Oak Path Fellows – Teachings of Jesus</title>
<link href="https://fonts.googleapis.com/css2?family=Raleway:wght@300;400;600;700&display=swap" rel="stylesheet">
<style>
  :root{
    --paper:#ffffff;
    --ink:#2b2b2b;
    --body:#5a5a5a;
    --heading:#333333;
  }
  html,body{margin:0;padding:0;overflow:hidden;background:var(--paper);}
  .page{
    width:847px;height:1200px;box-sizing:border-box;
    padding:40px 48px 0 50px;
    display:flex;gap:38px;overflow:hidden;
    font-family:"Raleway",sans-serif;color:var(--body);
    font-size:12.3px;line-height:16.2px;
  }
  .column{flex:1;}
  .column p{margin:0 0 1px;}
  .column p.indent{text-indent:16px;}
  .label{font-weight:700;color:var(--ink);}
  .section-title{
    font-weight:300;color:var(--heading);
    font-size:38px;line-height:44px;margin:40px 0 22px;
  }
  .section-subtitle{
    font-weight:600;color:var(--heading);
    font-size:22px;line-height:27px;margin:-14px 0 20px;
  }
</style>
</head>
<body>
<main class="page">
  <section class="column">
    <p><span class="label">Be wise as serpents and innocent as doves:</span> Matthew 10:16.</p>
    <p><span class="label">Do not worry about your life or material possessions:</span> Trust God to provide for your needs. Trust God to provide for your needs. Matthew 6:34</p>
    <p><span class="label">Lay up treasures in heaven:</span> Focus on building a spiritual inheritance rather than accumulating earthly wealth. Matthew 6:19-21.</p>
    <p><span class="label">Be a servant:</span> Seek greatness through humble service to others. Serve one another. Matthew 20:25-28</p>

    <h2 class="section-title">Prayer</h2>
    <p class="indent">Jesus provided guidance on prayer, teaching that it should be done in private and with sincerity (Matthew 6:5-8).</p>
    <p class="indent">He also linked prayer to having a forgiving heart (Mark 11:25; Matthew 18:18-20). HE encouraged praying with simple faith and persistence (Luke 11:5-13; Matthew 21:21-22).</p>
    <p><span class="label">Pray:</span> Engage in prayer consistently, with sincerity and according to Jesus' example.</p>
    <p><span class="label">Prayer for our enemies:</span> Luke 23:24; Matthew 5:44</p>
    <p><span class="label">Pray for others:</span> intercession</p>
    <p><span class="label">Pray for laborers:</span> Seek God to send workers into the harvest field of souls. Pray for kingdom laborers. Matthew 9:38, Luke 10:2</p>

    <h2 class="section-title">Regarding Outreach and Discipleship</h2>
    <p><span class="label">Go and make disciples of all nations:</span> Evangelize and teach others to follow Jesus' commands. This is a central command, emphasizing the importance of evangelism and discipleship. Matthew 28:18-20. Teach others to obey all that Jesus commanded. Passing on the teachings of Christ to new believers is a key aspect of discipleship.</p>
    <p><span class="label">Feed My Sheep:</span> Care for and nourish the spiritual lives of believers.</p>
    <p><span class="label">Receive God's power:</span> Be filled with the Holy Spirit to effectively carry out God's work.</p>

    <h2 class="section-title">Cautions and Warnings</h2>
    <p><span class="label">Beware of false prophets:</span> Be discerning and recognize those who may mislead others with false</p>
  </section>

  <section class="column">
    <p>teachings.</p>
    <p><span class="label">Beware of leaven (doctrine) of the Pharisees and Sadducees:</span> Avoid hypocrisy and legalism.</p>
    <p>Be alert and reliant on God's strength to overcome temptation.</p>
    <p><span class="label">Do not cast pearls before swine:</span> Use discretion and avoid sharing sacred things with those who may devalue or disrespect them.</p>

    <h2 class="section-title">Living as a Disciple</h2>
    <p><span class="label">Be merciful:</span> Show compassion to others, just as God is merciful. Act with kindness and compassion towards others. Luke 6:36</p>
    <p><span class="label">Care for those in distress:</span> Help the hungry, thirsty, strangers, naked, sick, and imprisoned.</p>
    <p class="indent">Recognize your own imperfections and avoid judging others harshly. Matthew 7:1-2. Luke 6:37 Focus on examining your own faults before criticizing others. He taught against judging others, stating that the standard by which you judge will be applied to you (Matthew 7:1-2).</p>
    <p><span class="label">Seek God's kingdom first:</span> Make God and his righteousness your highest priority. Prioritize God's reign and right way of living above all else. Found in Matthew 6:33.</p>
    <p><span class="label">Abide in JESUS:</span> John 15:4, John 6:35, 40, 47, John 14:21</p>
    <p><span class="label">Follow JESUS:</span> Matthew 4:19, Luke 5:28</p>

    <h2 class="section-title">Forgiveness</h2>
    <p class="section-subtitle">(Jesus Taught about the importance of both receiving and giving forgiveness)</p>
    <p><span class="label">Forgive others:</span> Matthew 6:12, 14, Mark 11:25-26, Luke 6:37</p>
    <p class="indent">Jesus emphasized that forgiveness is linked to forgiving others (Matthew 6:14-15).</p>
    <p class="indent">Forgiveness should be extended limitlessly to those who repent (Luke 17:3-4; Matthew 18:21-22).</p>
    <p class="indent">Forgiveness is also illustrated as the cancellation of debt (Matthew 18:23-35).</p>
  </section>
</main>
</body>
</html>
```